Package design for pain relief patches

The product I am trying to launch is a pain relief patch (think verdamil). I am targeting all age groups but want to keep it an upscale and clean look.

The brand is called Sorvel

The main challenge with my request is to keep the front simple, clean, concise while relaying the perception of a high quality product.

Another big challenge is to try relay all the information on the back (see "Must haves for what must be included), in a clean, concise way

Target Market(s)

all ages; but 18 - 100 age range

Industry/Entity Type

Health And Wellness

Font styles to use
Sans Serif

Colors

Designer to choose colors to be used in the design.

Requirements
Must have
• Front: All placements at the discretion of designer
• 1. The circle - must be prominent and have nothing in it
• 2. "zen" in japanese (image attached) somewhere (one of the bottom corners - but open to additional ideas - discretion of the designer)
• 3. company name (Sorvel) on package
• 4. "5 Pain Relief Patches"
• 5. Helps with Muscle Pain, Arthritis, Back Pain, Strains, Rheumatism
• Back: (Could be in bullets, or in a row - at the discretion of designer)
• 1. Uses: Helps with Muscle Pain, Arthritis, Back Pain, Strains, Rheumatism
• 2. Directions: Clean and dry affected area. Remove from backing film and apply to affected area no more than 3 - 4 times daily. Do not apply for more than 8 hours.
• 3. Warnings: Not for children under 12 years of age. Do apply on open wounds. If swallowed, get medical assistance immediately
• 4. Stop use and ask a doctor if: Conditions worsen, symptoms persist for more than 7 days, rash, itching, or excessive skin irritation occurs.
• 5. Keep out of reach of children
• 6. Active Ingredients: Camphor 1.2%, Menthol 5.7%, Methyl Salicylate 10%, Capsaicin 2.5%
Nice to have
• everything to be clean and concise
• Incorporating "霞舟" (means Kavo in japanese) somewhere on the package design
Should not have
• too much clutter
• zen in japanese should not be in the circle

```html
<!DOCTYPE html>
<html lang="en">
<head>
<meta charset="utf-8">
<title>Sorvel – 5 Pain Relief Patches</title>
<link rel="stylesheet" href="https://fonts.googleapis.com/css2?family=Roboto+Condensed:wght@400;500&family=Noto+Serif+JP:wght@500&display=swap">
<style>
  :root {
    --backdrop: #8a8a8a;
    --pouch: #f4f5f6;
    --pouch-edge: #e3e5e8;
    --brand-teal: #1ba394;
    --ink: #1b1b1b;
    --alert-red: #d4202c;
    --mark-tone: #cfd2d5;
    --figure-tone: #ddd3c4;
  }
  html, body {
    margin: 0;
    width: 1200px;
    height: 1200px;
    overflow: hidden;
    background: var(--backdrop);
  }
  .canvas {
    position: relative;
    width: 1200px;
    height: 1200px;
  }
  .pouch {
    position: absolute;
    left: 287px;
    top: 128px;
    width: 661px;
    height: 955px;
    background: linear-gradient(180deg, #fbfbfc 0%, var(--pouch) 55%, #eceef0 100%);
    border: 14px solid var(--pouch-edge);
    box-sizing: border-box;
    border-radius: 6px;
  }
  .brand-mark-area {
    position: absolute;
    left: 209px;
    top: 58px;
    width: 188px;
    height: 188px;
    background: radial-gradient(circle, #e9ebed 0%, var(--mark-tone) 100%);
  }
  .brand-name {
    position: absolute;
    left: 0;
    right: 0;
    top: 286px;
    margin: 0;
    text-align: center;
    font-family: "Roboto Condensed", Arial, sans-serif;
    font-weight: 500;
    font-size: 120px;
    line-height: 1;
    color: var(--ink);
  }
  .pack-count {
    position: absolute;
    left: 0;
    right: 0;
    top: 418px;
    text-align: center;
    font-family: "Roboto Condensed", Arial, sans-serif;
    font-weight: 500;
    font-size: 30px;
    line-height: 1;
    color: var(--ink);
  }
  .helps-label {
    position: absolute;
    left: 206px;
    top: 477px;
    width: 232px;
    height: 53px;
    background: var(--brand-teal);
    color: var(--ink);
    font-family: "Roboto Condensed", Arial, sans-serif;
    font-weight: 500;
    font-size: 40px;
    line-height: 53px;
    text-align: center;
  }
  .uses-list {
    position: absolute;
    left: 117px;
    top: 545px;
    margin: 0;
    padding: 0;
    list-style: none;
    font-family: "Roboto Condensed", Arial, sans-serif;
    font-size: 37px;
    color: var(--alert-red);
  }
  .uses-list li {
    display: flex;
    align-items: center;
    height: 51px;
  }
  .tick-icon {
    width: 28px;
    height: 28px;
    margin-right: 27px;
    flex: none;
  }
  .application-figure {
    position: absolute;
    left: 204px;
    top: 711px;
    width: 206px;
    height: 186px;
    background: linear-gradient(180deg, #e4dbcd 0%, var(--figure-tone) 100%);
    border-radius: 70px 70px 8px 8px;
  }
  .kanji {
    position: absolute;
    font-family: "Noto Serif JP", serif;
    font-weight: 500;
    color: var(--ink);
    line-height: 1;
  }
  .kanji-zen {
    left: 57px;
    top: 848px;
    font-size: 52px;
  }
  .kanji-name {
    right: 51px;
    top: 853px;
    font-size: 42px;
  }
</style>
</head>
<body>
<div class="canvas">
  <section class="pouch">
    <div class="brand-mark-area" role="img" aria-label="Brush-drawn open circle brand symbol"></div>
    <h1 class="brand-name">Sorvel</h1>
    <div class="pack-count">5 Pain Relief Patches</div>
    <div class="helps-label">Helps with</div>
    <ul class="uses-list">
      <li><svg class="tick-icon" viewBox="0 0 28 28" aria-hidden="true"><circle cx="14" cy="14" r="11.5" fill="none" stroke="currentColor" stroke-width="2.6"/><path d="M8.5 14.5 L12.8 18.5 L20 9.5" fill="none" stroke="currentColor" stroke-width="2.6" stroke-linecap="round" stroke-linejoin="round"/></svg>Strains, Back Pain</li>
      <li><svg class="tick-icon" viewBox="0 0 28 28" aria-hidden="true"><circle cx="14" cy="14" r="11.5" fill="none" stroke="currentColor" stroke-width="2.6"/><path d="M8.5 14.5 L12.8 18.5 L20 9.5" fill="none" stroke="currentColor" stroke-width="2.6" stroke-linecap="round" stroke-linejoin="round"/></svg>Arthritis, Muscle Pain</li>
      <li><svg class="tick-icon" viewBox="0 0 28 28" aria-hidden="true"><circle cx="14" cy="14" r="11.5" fill="none" stroke="currentColor" stroke-width="2.6"/><path d="M8.5 14.5 L12.8 18.5 L20 9.5" fill="none" stroke="currentColor" stroke-width="2.6" stroke-linecap="round" stroke-linejoin="round"/></svg>Rheumatism</li>
    </ul>
    <div class="application-figure" role="img" aria-label="Illustration of a person's head and shoulders with a patch applied to the neck"></div>
    <div class="kanji kanji-zen" lang="ja">禅</div>
    <div class="kanji kanji-name" lang="ja">霞舟</div>
  </section>
</div>
</body>
</html>
```